New company website for Redfern Hollow Building Company

We're looking to build a new company website that customers can use to contact us, get quotes, view past projects (renovations, additions, new construction, etc.), & learn more about our business. We want to use WordPress for our website and have already purchased the Divi theme (by Quillmark Studio). Using that theme isn't required but we already have several examples of websites that we want to model our site after that use this theme. The "look" we're after is simple, light, & clean.

Target Market(s)

Residential remodeling, renovations, and new construction.

Industry/Entity Type

Residential Construction

Coding

Coded - Design and coding required

Number of Pages Required

5+ page

Font styles to use
Sans Serif

Colors
33a6d7
aaaaaa

Requirements
Must have
• We require the website to be coded using the Divi theme. We'll be upgrading the project to include this today or tomorrow.
• The navigation bar should be static & remain at the top of the page. When scrolling we'd like the logo & info in the nav bar to size down. Here's an example of a site that does this: https://tovamerihomes.example/
Nice to have
• In the gallery with pictures of our finished product/jobs, when you mouse over the image, we'd like there to be additional info that shows up. For example, look at this gallery: https://tovamerihomes.example/projectcategories/kitchens/ We'll add a name/location of the job like: "Garvey kitchen - Apex, N.C."
• If you go to this website: https://plinvorworks.example/ and scroll down to the pictures, we like how the picture moves and is interactive.

```html
<!DOCTYPE html>
<html lang="en">
<head>
<meta charset="utf-8">
<title>Redfern Hollow Building Company</title>
<link href="https://fonts.googleapis.com/css2?family=Asap:wght@500;600;700&family=Lato:wght@400;700&display=swap" rel="stylesheet">
<style>
:root{
  --blue:#33a6d7;
  --blue-dark:#2b93c2;
  --grey:#aaaaaa;
  --card:#efefef;
  --text:#555555;
  --heading:#333333;
  --dark:#333333;
  --white:#ffffff;
}
*{box-sizing:border-box;margin:0;padding:0}
html,body{width:1200px;height:4100px;overflow:hidden;background:var(--white)}
body{position:relative;font-family:"Lato",sans-serif;color:var(--text)}
.abs{position:absolute}
.photo{position:absolute}

/* header */
.brand{left:77px;top:28px;font-family:"Asap",sans-serif;font-weight:700;color:var(--heading);line-height:1}
.brand-name{font-size:38px;letter-spacing:1px}
.brand-sub{font-size:17px;letter-spacing:7.5px;margin-top:2px}
.call{right:77px;top:22px;display:flex;align-items:center;gap:16px}
.call-icon{width:56px;height:56px;border:2px solid var(--blue);border-radius:50%;display:flex;align-items:center;justify-content:center}
.call-label{font-size:15px;color:var(--text);letter-spacing:.5px}
.call-number{font-size:26px;color:var(--heading);font-weight:700;margin-top:2px}

.nav{left:0;top:104px;width:1200px;height:56px;background:var(--dark);display:flex;padding-left:88px;z-index:2}
.nav a{color:var(--white);text-decoration:none;font-size:15px;letter-spacing:.5px;display:flex;align-items:center;padding:0 20px;height:56px;text-transform:uppercase}
.nav a.active{background:var(--blue);height:64px;clip-path:polygon(0 0,100% 0,100% 86%,50% 100%,0 86%)}

.hero{left:0;top:104px;width:1200px;height:606px;background:linear-gradient(180deg,#4a4a48 0%,#6d6a66 45%,#5b5852 100%)}
.hero-title{left:0;top:355px;width:1200px;text-align:center;font-family:"Asap",sans-serif;font-weight:700;font-size:56px;color:var(--white);letter-spacing:2px}
.hero-sub{left:0;top:440px;width:1200px;text-align:center;font-size:22px;color:var(--white)}

/* section labels */
.label{background:var(--blue);color:var(--white);font-family:"Asap",sans-serif;font-weight:600;font-size:34px;letter-spacing:1px;display:flex;align-items:center;padding-left:78px}
.label::after{content:"";position:absolute;right:40px;top:22px;width:2px;height:46px;background:var(--white)}
.section-title{left:0;width:1200px;text-align:center;font-family:"Asap",sans-serif;font-weight:700;font-size:34px;color:var(--blue);letter-spacing:.5px}

/* about */
.about-photo{left:77px;top:809px;width:459px;height:467px;background:linear-gradient(160deg,#d9dcdc 0%,#8f8b86 50%,#4a3a30 100%)}
.about-text{left:623px;top:962px;width:500px;font-size:15.5px;line-height:25px;color:#666}
.about-text p+p{margin-top:14px}
.btn{left:623px;top:1203px;width:186px;height:46px;border-radius:23px;background:var(--blue);color:var(--white);font-family:"Asap",sans-serif;font-weight:700;font-size:19px;display:flex;align-items:center;justify-content:center}

/* cards */
.card{position:absolute;width:240px;background:var(--card);border-radius:6px;text-align:center}
.process-card{top:1407px;height:266px}
.diamond{position:absolute;left:85px;top:32px;width:70px;height:70px;display:flex;align-items:center;justify-content:center}
.diamond::before{content:"";position:absolute;inset:10px;background:var(--white);transform:rotate(45deg);border-radius:6px}
.diamond span{position:relative;font-family:"Asap",sans-serif;font-size:30px;color:var(--blue)}
.card-title{position:absolute;top:152px;width:100%;font-size:18px;color:var(--heading);text-transform:uppercase;letter-spacing:.3px}
.card-text{position:absolute;top:188px;left:20px;right:20px;font-size:14px;line-height:23px;color:#666}

/* specialities */
.spec-photo{left:664px;top:1771px;width:457px;height:500px;background:linear-gradient(170deg,#d8d4cc 0%,#b49573 55%,#7f6448 100%)}
.spec-item{right:738px;width:400px;text-align:right}
.spec-item h3{font-family:"Lato",sans-serif;font-weight:400;font-size:22px;color:var(--blue)}
.spec-item p{font-size:14px;line-height:24px;color:#666;margin-top:8px}
.spec-icon{left:500px;width:96px;height:96px}

/* banner */
.banner{left:0;top:2367px;width:1200px;height:229px;background:linear-gradient(90deg,#2b2f36 0%,#474b50 55%,#2e3238 100%)}
.banner-text{left:77px;top:2432px;width:640px;font-family:"Asap",sans-serif;font-weight:700;font-size:33px;line-height:52px;color:var(--white)}

/* team */
.team-card{top:2706px;height:350px;overflow:hidden}
.team-top{position:absolute;left:0;top:0;width:240px;height:120px}
.avatar{position:absolute;left:70px;top:45px;width:100px;height:100px;border-radius:50%;border:4px solid var(--white);background:linear-gradient(180deg,#6fa36a 0%,#3f6e49 100%)}
.team-name{position:absolute;top:177px;width:100%;font-size:22px;color:var(--blue)}
.team-text{position:absolute;top:213px;left:22px;right:22px;font-size:14px;line-height:24px;color:#666}
.team-link{position:absolute;top:300px;width:100%;font-size:14px;font-weight:700;color:var(--blue);text-decoration:underline}

/* portfolio */
.port-main{left:77px;top:3157px;width:459px;height:361px;background:linear-gradient(180deg,#a9c4dc 0%,#e9ecef 45%,#6c8a4e 100%)}
.filters{left:634px;top:3312px;font-size:15px;color:#666;word-spacing:2px}
.filters .on{color:var(--blue)}
.filters i{font-style:normal;color:#999;margin:0 6px}
.thumb{position:absolute;width:238px;height:156px}

/* newsletter + footer */
.newsletter{left:0;top:3785px;width:1200px;height:105px;background:var(--blue)}
.news-title{left:77px;top:3822px;font-size:26px;font-weight:700;color:var(--white);letter-spacing:.5px}
.news-input{left:698px;top:3820px;width:290px;height:38px;background:var(--white);border-radius:19px 0 0 19px;font-size:14px;color:#999;display:flex;align-items:center;padding-left:22px}
.news-btn{left:988px;top:3820px;width:134px;height:38px;background:var(--dark);border-radius:0 19px 19px 0;color:var(--white);font-size:17px;font-weight:700;display:flex;align-items:center;justify-content:center}
.footer{left:0;top:3890px;width:1200px;height:210px;background:var(--dark)}
.socials{left:0;top:3926px;width:1200px;display:flex;justify-content:center;gap:26px}
.socials span{width:50px;height:50px;border-radius:50%;background:var(--white)}
.foot-nav{left:0;top:4004px;width:1200px;display:flex;justify-content:center;gap:28px;font-size:15px;color:var(--white)}
.copy{left:0;top:4046px;width:1200px;text-align:center;font-size:14px;color:var(--white);letter-spacing:.5px}
</style>
</head>
<body>

<header>
  <div class="abs brand">
    <div class="brand-name">REDFERN HOLLOW</div>
    <div class="brand-sub">BUILDING COMPANY</div>
  </div>
  <div class="abs call">
    <div class="call-icon">
      <svg width="26" height="26" viewBox="0 0 24 24" fill="#33a6d7"><path d="M6.6 10.8a15.2 15.2 0 0 0 6.6 6.6l2.2-2.2a1 1 0 0 1 1-.25 11.4 11.4 0 0 0 3.6.57 1 1 0 0 1 1 1V20a1 1 0 0 1-1 1A17 17 0 0 1 3 4a1 1 0 0 1 1-1h3.5a1 1 0 0 1 1 1c0 1.25.2 2.45.57 3.570a1 1 0 0 1-.25 1z"/></svg>
    </div>
    <div>
      <div class="call-label">CALL US NOW</div>
      <div class="call-number">123 456 7890</div>
    </div>
  </div>
</header>

<div class="photo hero" role="img" aria-label="Bright white kitchen with island, pendant lights and stainless appliances"></div>
<nav class="abs nav">
  <a class="active">Home</a><a>Getting Started</a><a>Who We Are</a><a>Specialities</a><a>Portfolio</a><a>Contact</a>
</nav>
<h1 class="abs hero-title">REDFERN HOLLOW</h1>
<p class="abs hero-sub">Lorem Ipsum is simply dummy text of the printing.</p>

<!-- about -->
<div class="photo about-photo" role="img" aria-label="Modern kitchen with dark wood island and bar stools"></div>
<h2 class="abs label" style="left:344px;top:831px;width:375px;height:90px">ABOUT US</h2>
<div class="abs about-text">
  <p>Lorem Ipsum is simply dummy text of the printing and typesetting industry. Lorem Ipsum has been the industry's standard dummy text ever since the 1500s, when an unknown printer took a galley of type and scrambled it to make a type specimen book. It has survived not only five centuries, but also the leap into electronic typesetting</p>
  <p>Lorem Ipsum is simply dummy text of the printing and typesetting industry. Lorem Ipsum has been the industry's standard dummy text ever since the 1500s, when an unknown printer took a galley of type.</p>
</div>
<div class="abs btn">KNOW MORE</div>

<!-- process -->
<h2 class="abs section-title" style="top:1345px">OUR PROCESS</h2>
<div class="card process-card" style="left:77px"><div class="diamond"><span>01</span></div><div class="card-title">Creative Ideas</div><div class="card-text">Lorem Ipsum is simply dummy text of the printing.</div></div>
<div class="card process-card" style="left:347px"><div class="diamond"><span>02</span></div><div class="card-title">Planning</div><div class="card-text">Lorem Ipsum is simply dummy text of the printing.</div></div>
<div class="card process-card" style="left:615px"><div class="diamond"><span>03</span></div><div class="card-title">Safe Work</div><div class="card-text">Lorem Ipsum is simply dummy text of the printing.</div></div>
<div class="card process-card" style="left:883px"><div class="diamond"><span>04</span></div><div class="card-title">Best Quality</div><div class="card-text">Lorem Ipsum is simply dummy text of the printing.</div></div>

<!-- specialities -->
<div class="photo spec-photo" role="img" aria-label="Bathroom with twin oval mirrors, wood vanity and corner tub"></div>
<h2 class="abs label" style="left:465px;top:1796px;width:371px;height:90px;padding-left:80px">SPECIALITIES</h2>

<div class="abs spec-item" style="top:1940px"><h3>Remodeling</h3><p>Lorem Ipsum is simply dummy text of the printing<br>and typesetting industry. Lorem Ipsum has been.</p></div>
<div class="abs spec-item" style="top:2052px"><h3>New home construction</h3><p>Lorem Ipsum is simply dummy text of the printing<br>and typesetting industry. Lorem Ipsum has been.</p></div>
<div class="abs spec-item" style="top:2168px"><h3>Additions</h3><p>Lorem Ipsum is simply dummy text of the printing<br>and typesetting industry. Lorem Ipsum has been.</p></div>

<svg class="abs spec-icon" style="top:1934px" viewBox="0 0 96 96"><rect x="20" y="20" width="56" height="56" rx="8" transform="rotate(45 48 48)" fill="none" stroke="#33a6d7" stroke-width="2"/><path d="M34 48 48 36 62 48M38 45v15h20V45" fill="none" stroke="#33a6d7" stroke-width="2.5"/></svg>
<svg class="abs spec-icon" style="top:2046px" viewBox="0 0 96 96"><rect x="20" y="20" width="56" height="56" rx="8" transform="rotate(45 48 48)" fill="none" stroke="#33a6d7" stroke-width="2"/><path d="M34 40h20v18H34zM54 46h8v12h-8M38 46h6v6h-6" fill="none" stroke="#33a6d7" stroke-width="2.5"/></svg>
<svg class="abs spec-icon" style="top:2160px" viewBox="0 0 96 96"><rect x="20" y="20" width="56" height="56" rx="8" transform="rotate(45 48 48)" fill="none" stroke="#33a6d7" stroke-width="2"/><path d="M34 48 48 36 62 48H58v12H38V48z" fill="#33a6d7"/><rect x="45" y="51" width="6" height="9" fill="#fff"/></svg>

<!-- banner -->
<div class="photo banner" role="img" aria-label="Finished home exterior at dusk with a hard hat and rolled plans in the foreground"></div>
<p class="abs banner-text">Lorem Ipsum is simply dummy text of the printing and typesetting.</p>

<!-- team -->
<h2 class="abs section-title" style="top:2643px">OUR TEAM</h2>
<div class="card team-card" style="left:77px">
  <svg class="team-top" viewBox="0 0 240 120"><polygon points="0,0 240,0 240,38 120,95 0,38" fill="#33a6d7"/></svg>
  <div class="avatar" role="img" aria-label="Portrait of Owen Castell"></div>
  <div class="team-name">Owen Castell</div>
  <div class="team-text">President Owen Castell manages the Brookline Floor &amp; Tile team with a passion...</div>
  <div class="team-link">KNOW MORE</div>
</div>
<div class="card team-card" style="left:347px">
  <svg class="team-top" viewBox="0 0 240 120"><polygon points="0,0 240,0 240,38 120,95 0,38" fill="#33a6d7"/></svg>
  <div class="avatar" role="img" aria-label="Portrait of Miles Castell"></div>
  <div class="team-name">Miles Castell</div>
  <div class="team-text">Founder Miles Castell divides his time between directing sales and...</div>
  <div class="team-link">KNOW MORE</div>
</div>
<div class="card team-card" style="left:615px">
  <svg class="team-top" viewBox="0 0 240 120"><polygon points="0,0 240,0 240,38 120,95 0,38" fill="#33a6d7"/></svg>
  <div class="avatar" role="img" aria-label="Portrait of Desmond Hartwell"></div>
  <div class="team-name">Desmond Hartwell</div>
  <div class="team-text">Des manages Brookline Floor and Tile's projects- from scheduling workers to final...</div>
  <div class="team-link">KNOW MORE</div>
</div>
<div class="card team-card" style="left:883px">
  <svg class="team-top" viewBox="0 0 240 120"><polygon points="0,0 240,0 240,38 120,95 0,38" fill="#33a6d7"/></svg>
  <div class="avatar" role="img" aria-label="Portrait of Owen Castell"></div>
  <div class="team-name">Owen Castell</div>
  <div class="team-text">A Larkspur native and Eastfield State graduate with a BS in Business...</div>
  <div class="team-link">KNOW MORE</div>
</div>

<!-- portfolio -->
<div class="photo port-main" role="img" aria-label="White two-storey house with wraparound porch"></div>
<h2 class="abs label" style="left:413px;top:3176px;width:374px;height:93px;padding-left:78px">PORTFOLIO</h2>
<div class="abs filters"><span class="on">All</span><i>/</i>Before and after<i>/</i>Kitchens<i>/</i>Bathrooms<i>/</i>Whole house</div>

<div class="thumb" style="left:615px;top:3362px;background:linear-gradient(150deg,#6b5a48,#2e2620)" role="img" aria-label="Dark wood kitchen project"></div>
<div class="thumb" style="left:883px;top:3362px;background:linear-gradient(150deg,#e4e2de,#8e7e6c)" role="img" aria-label="White kitchen with island project"></div>
<div class="thumb" style="left:77px;top:3550px;background:linear-gradient(150deg,#e8e8e6,#a49c90)" role="img" aria-label="Open white kitchen project"></div>
<div class="thumb" style="left:344px;top:3550px;background:linear-gradient(150deg,#b8a894,#5f4e3d)" role="img" aria-label="Living room project"></div>
<div class="thumb" style="left:615px;top:3550px;background:linear-gradient(150deg,#c9c3b8,#6c5a46)" role="img" aria-label="Bathroom vanity project"></div>
<div class="thumb" style="left:883px;top:3550px;background:linear-gradient(150deg,#a78e72,#3f3328)" role="img" aria-label="Dining room project"></div>

<!-- newsletter -->
<div class="abs newsletter"></div>
<div class="abs news-title">SUBSCRIBE TO OUR NEWSLETTER</div>
<div class="abs news-input">Enter your email</div>
<div class="abs news-btn">SUBSCRIBE</div>

<!-- footer -->
<footer>
  <div class="abs footer"></div>
  <div class="abs socials"><span></span><span></span><span></span><span></span></div>
  <div class="abs foot-nav"><span>Home</span><span>Getting Started</span><span>Who We are</span><span>Specialities</span><span>Portfolio</span><span>Contact</span></div>
  <div class="abs copy">©REDFERN HOLLOW- 2018. All Rights Reserved.</div>
</footer>

</body>
</html>
```